Halvern Aviation Group - "Coming Soon" Main Company Webpage

Design a main webpage that can be posted while a fully functional website is constructed. The design should be created to convey a sense of luxury and exclusivity. The main page should contain only one photo as the background. The photo I believe to show "luxury" and "Exclusivity" is listed as "Global Luxury Photo". I have included two other photos as well to aid in providing a variety of presentations.
The "Member PQTR" logo should appear somewhere on the main page but be less prevalent than the main company logo. "Coming Soon" should also appear to convey that a website is being constructed.
Tabs for the website:
- Aircraft Management
- Aircraft Sales
- Pilot Services
- Charter
- Flight Training

```html
<!DOCTYPE html>
<html lang="en">
<head>
<meta charset="utf-8">
<title>Halvern Aviation Group — Coming Soon</title>
<link rel="stylesheet" href="https://fonts.googleapis.com/css2?family=Montserrat:wght@200;300;400;600;700&display=swap">
<style>
  :root {
    --brand-blue: #1b63b0;
    --ink: #1a1d22;
    --paper: #ffffff;
    --night: #0e1116;
    --sky-dark: #4a4c50;
    --sky-mid: #66686c;
    --sky-light: #8a8c90;
    --line: rgba(255,255,255,0.85);
  }
  * { box-sizing: border-box; margin: 0; padding: 0; }
  html, body { width: 1200px; height: 675px; overflow: hidden; background: var(--paper); }
  body { font-family: "Montserrat", sans-serif; position: relative; }

  .site-header {
    position: absolute; left: 0; top: 0; width: 1200px; height: 109px;
    background: var(--paper);
    display: flex; align-items: center; justify-content: center;
  }
  .brand-name {
    font-family: "Montserrat", sans-serif;
    font-weight: 700; font-size: 26px; letter-spacing: 1.5px;
    color: var(--brand-blue); text-transform: uppercase;
  }

  .hero {
    position: absolute; left: 0; top: 109px; width: 1200px; height: 551px;
    overflow: hidden;
  }
  .hero-photo {
    position: absolute; inset: 0;
    background:
      radial-gradient(ellipse 60% 70% at 85% 75%, var(--sky-light) 0%, rgba(138,140,144,0) 70%),
      linear-gradient(180deg, var(--sky-dark) 0%, var(--sky-mid) 45%, var(--sky-dark) 100%);
  }

  .main-nav {
    position: absolute; top: 23px; left: 0; width: 1200px; height: 34px;
  }
  .nav-tab {
    position: absolute; top: 0; height: 34px;
    display: flex; align-items: center; justify-content: center;
    border: 1px solid var(--line);
    color: #fff; font-size: 17.5px; font-weight: 300; letter-spacing: 0.3px;
    text-transform: uppercase; white-space: nowrap;
  }
  .nav-tab.is-active {
    background: var(--brand-blue); border-color: var(--brand-blue);
    font-weight: 700;
  }
  .tab-management { left: 88px; width: 269px; }
  .tab-sales { left: 369px; width: 190px; }
  .tab-pilots { left: 570px; width: 191px; }
  .tab-charter { left: 771px; width: 127px; }
  .tab-training { left: 908px; width: 198px; }

  .coming-soon {
    position: absolute; left: 0; top: 190px; width: 1200px;
    text-align: center; color: #fff;
    font-size: 58px; font-weight: 300; letter-spacing: 0.5px;
  }

  .membership {
    position: absolute; left: 32px; top: 508px;
    display: flex; align-items: flex-end; gap: 7px; color: #fff;
  }
  .membership-mark {
    width: 34px; height: 24px; border-radius: 50%;
    border: 2px solid #fff; margin-bottom: 1px;
  }
  .membership-text { display: flex; flex-direction: column; line-height: 1; }
  .membership-label { font-size: 8px; font-weight: 400; margin-bottom: 3px; }
  .membership-name { font-size: 22px; font-weight: 300; letter-spacing: 3px; }

  .social-links {
    position: absolute; right: 32px; top: 522px;
    display: flex; gap: 32px;
  }
  .social-dot {
    width: 18px; height: 18px; border-radius: 50%;
    border: 2px solid #fff; display: block;
  }

  .footer-band {
    position: absolute; left: 0; top: 660px; width: 1200px; height: 15px;
    display: flex;
  }
  .footer-band .band-blue { width: 599px; background: var(--brand-blue); }
  .footer-band .band-night { flex: 1; background: var(--night); }
</style>
</head>
<body>
  <header class="site-header">
    <span class="brand-name">Halvern Aviation Group</span>
  </header>

  <main class="hero">
    <div class="hero-photo" role="img" aria-label="Photograph of a white private jet's tail, engine and wing under an overcast grey sky"></div>

    <nav class="main-nav">
      <span class="nav-tab tab-management is-active">Aircraft Management</span>
      <span class="nav-tab tab-sales">Aircraft Sales</span>
      <span class="nav-tab tab-pilots">Pilot Services</span>
      <span class="nav-tab tab-charter">Charter</span>
      <span class="nav-tab tab-training">Flight Training</span>
    </nav>

    <h1 class="coming-soon">Coming Soon</h1>

    <div class="membership">
      <span class="membership-mark"></span>
      <span class="membership-text">
        <span class="membership-label">member of</span>
        <span class="membership-name">PQTR</span>
      </span>
    </div>

    <div class="social-links">
      <span class="social-dot" aria-label="Social network link"></span>
      <span class="social-dot" aria-label="Social network link"></span>
      <span class="social-dot" aria-label="Social network link"></span>
    </div>
  </main>

  <div class="footer-band">
    <span class="band-blue"></span>
    <span class="band-night"></span>
  </div>
</body>
</html>
```